Tallowick Limited Business Card

We need a business card for a new company based in Essex, United Kingdom. We develop and manufacture educational games. The business card needs to match the company brand and logo and the colour scheme.
My company makes educational board games to be played by the family or used by teachers
The games are tile based number game

Target Market(s)

Parents, teachers, schools and children

Industry/Entity Type

Games

Contact Information for Business Card

Company Name - Tallowick Limited
Director - Damian Prouse
Registered Office - 3 Marsh Court, 142 Quarry Lane, Brindleford, Essex, CM7 4XR
Phone Number - 07950 000 318
Email - Enquiries@Tallowick.example
Website - www.Tallowick.example
Company Number - 00000000

Font styles to use
Sans Serif

Colors
00a990
ffffff

Requirements
Must have
• Same colour scheme as the attachments - green and white
• Same font style for Tallowick
• Images of the number tiles similar to the attachments
• extra details
• The colour is Cyan - 82 Magenta - 24 Yellow - 44 Black - 2
• I have attached some of the font styles use on my website and alos my LOGO
Nice to have
• Image of the number "1" tag as seen on the website

```html
<!DOCTYPE html>
<html lang="en">
<head>
<meta charset="utf-8">
<title>Tallowick Limited – Business Card</title>
<link rel="stylesheet" href="https://fonts.googleapis.com/css2?family=Catamaran:wght@400;600&family=Titillium+Web:wght@700&family=Open+Sans:wght@400&display=swap">
<style>
  :root {
    --teal: #3f8d8f;
    --teal-dark: #2f7a7e;
    --teal-light: #7db7b8;
    --teal-mid: #5aa2ad;
    --ink: #333a3d;
    --paper: #ffffff;
    --paper-shade: #e4eaec;
    --backdrop: #8c8c8c;
  }
  * { box-sizing: border-box; margin: 0; padding: 0; }
  html, body { width: 1200px; height: 1200px; overflow: hidden; }
  body {
    background: var(--backdrop);
    font-family: "Catamaran", sans-serif;
    display: flex;
    flex-direction: column;
    align-items: center;
    justify-content: center;
    gap: 20px;
  }
  .card {
    position: relative;
    width: 940px;
    height: 580px;
    overflow: hidden;
    box-shadow: 0 6px 18px rgba(0,0,0,.25);
  }

  /* Front */
  .card--front {
    background: linear-gradient(180deg, var(--paper) 0%, var(--paper) 45%, var(--paper-shade) 100%);
  }
  .brand {
    position: absolute;
    left: 50px;
    top: 70px;
    color: var(--teal);
  }
  .brand__name {
    font-weight: 600;
    font-size: 70px;
    line-height: 1;
  }
  .brand__tagline {
    font-weight: 400;
    font-size: 24px;
    line-height: 1;
    margin-top: 8px;
  }
  .person {
    position: absolute;
    right: 54px;
    top: 72px;
    text-align: right;
  }
  .person__name {
    font-family: "Titillium Web", sans-serif;
    font-weight: 700;
    font-size: 42px;
    line-height: 1;
    color: var(--teal);
    letter-spacing: 1px;
  }
  .person__role {
    font-family: "Open Sans", sans-serif;
    font-size: 30px;
    line-height: 1.3;
    color: var(--ink);
  }
  .product-shot {
    position: absolute;
    left: 70px;
    top: 250px;
    width: 230px;
    height: 230px;
    border-radius: 30px;
    transform: rotate(-30deg);
    background: linear-gradient(160deg, #5ea6a8 0%, #4a9296 100%);
    box-shadow: 0 14px 16px -10px rgba(0,0,0,.25);
  }
  .product-card {
    position: absolute;
    left: 300px;
    top: 225px;
    width: 80px;
    height: 110px;
    border-radius: 4px;
    transform: rotate(-30deg);
    background: linear-gradient(180deg, #5aa2a5 0%, #e6f0f0 100%);
  }
  .contact {
    position: absolute;
    right: 54px;
    top: 290px;
    list-style: none;
    color: var(--ink);
    font-size: 28px;
    line-height: 1.35;
  }
  .contact__item {
    display: flex;
    justify-content: flex-end;
    align-items: center;
    gap: 20px;
  }
  .contact__text { text-align: right; }
  .contact__item--address { margin-bottom: 22px; }
  .contact__icon {
    width: 26px;
    height: 26px;
    flex: none;
    color: var(--teal);
  }
  .accent-bar {
    position: absolute;
    right: 0;
    top: 292px;
    width: 16px;
    height: 246px;
    background: var(--teal);
  }

  /* Back */
  .card--back {
    background: linear-gradient(160deg, var(--teal-light) 0%, var(--teal-mid) 60%, var(--teal-dark) 100%);
    color: var(--paper);
  }
  .back-lockup {
    position: absolute;
    left: 50%;
    top: 50%;
    transform: translate(-50%, -50%) rotate(-32deg);
    white-space: nowrap;
  }
  .back-lockup__name {
    font-weight: 600;
    font-size: 140px;
    line-height: .95;
  }
  .back-lockup__tagline {
    font-size: 40px;
    line-height: 1.1;
    font-weight: 400;
    letter-spacing: 1px;
  }
  .back-lockup__web {
    font-size: 28px;
    letter-spacing: 10px;
    margin-top: 24px;
    margin-left: 110px;
  }
</style>
</head>
<body>

<section class="card card--front" aria-label="Business card front">
  <div class="brand">
    <div class="brand__name">Tallowick</div>
    <div class="brand__tagline">CLEVER FAMILY TILE GAMES</div>
  </div>

  <div class="person">
    <div class="person__name">DAMIAN PROUSE</div>
    <div class="person__role">Director</div>
  </div>

  <div class="product-shot" role="img" aria-label="Product photo of the teal number-tile game case with its number 1 tag"></div>
  <div class="product-card" role="img" aria-label="Product photo of a game rules card"></div>

  <ul class="contact">
    <li class="contact__item contact__item--address">
      <span class="contact__text">3 Marsh Court, 142 Quarry Lane<br>Brindleford, Essex, CM7 4XR</span>
      <svg class="contact__icon" viewBox="0 0 24 24" aria-hidden="true"><path d="M12 2a6 6 0 0 0-6 6c0 4.5 6 10 6 10s6-5.5 6-10a6 6 0 0 0-6-6z" fill="none" stroke="currentColor" stroke-width="2"/><circle cx="12" cy="8" r="2.2" fill="currentColor"/><ellipse cx="12" cy="21" rx="7" ry="1.8" fill="currentColor"/></svg>
    </li>
    <li class="contact__item">
      <span class="contact__text">07950 000 318</span>
      <svg class="contact__icon" viewBox="0 0 24 24" aria-hidden="true"><path d="M6.5 3.5l3 3-2 2.5c1.2 2.6 3 4.4 5.5 5.5l2.5-2 3 3-2.2 2.8C10.5 18 6 13.5 3.7 5.7z" fill="none" stroke="currentColor" stroke-width="2" stroke-linejoin="round"/></svg>
    </li>
    <li class="contact__item">
      <span class="contact__text">Enquiries@Tallowick.example</span>
      <svg class="contact__icon" viewBox="0 0 24 24" aria-hidden="true"><rect x="3" y="6" width="18" height="13" rx="1.5" fill="none" stroke="currentColor" stroke-width="2"/><path d="M3.5 7l8.5 6.5L20.5 7" fill="none" stroke="currentColor" stroke-width="2"/></svg>
    </li>
    <li class="contact__item">
      <span class="contact__text">www.Tallowick.example</span>
      <svg class="contact__icon" viewBox="0 0 24 24" aria-hidden="true"><circle cx="12" cy="12" r="9" fill="none" stroke="currentColor" stroke-width="2"/><path d="M3 12h18M12 3c3 3 3 15 0 18M12 3c-3 3-3 15 0 18" fill="none" stroke="currentColor" stroke-width="1.6"/></svg>
    </li>
    <li class="contact__item">
      <span class="contact__text">Company Number - 00000000</span>
      <svg class="contact__icon" viewBox="0 0 24 24" aria-hidden="true"><rect x="4" y="3" width="6" height="18" rx="2" fill="none" stroke="currentColor" stroke-width="2"/><rect x="10" y="7" width="10" height="14" rx="1.5" fill="none" stroke="currentColor" stroke-width="2"/><path d="M13 11h4M13 14h4M13 17h4" stroke="currentColor" stroke-width="1.6"/></svg>
    </li>
  </ul>

  <div class="accent-bar"></div>
</section>

<section class="card card--back" aria-label="Business card back">
  <div class="back-lockup">
    <div class="back-lockup__name">Tallowick</div>
    <div class="back-lockup__tagline">CLEVER FAMILY TILE GAMES</div>
    <div class="back-lockup__web">www.Tallowick.example</div>
  </div>
</section>

</body>
</html>
```